Nonna's Granary - Flour Bag Packing for Fit and Healthy Flour

Nonna's Granary is a family owned company that was incorporated in honor of our grandfather who is in the pic below. We would like to incorporate that picture into the packaging design. We would also like for the logo to represent a modern/fit lifestyle that is unique from the current competition.

Nonna's flour is a newly practiced style of milling that allows for flour to be consumed in its natural/organic state. We don't not bleach, chemically treat or add any enriched/preservative additives to our flour. This allows for freshness (our priority) and the natural flavors of the nutty grain to seep into our flour.

Our flour contains all the nutritional value that comes from all the components of Wheat Family Grains.

Our Family has been in the flour business for 60+ years and we established our mill in Debar Macedonia in 1998.

100% Organic
Non GMO
Family Owned
Stone Milled
Banner (Product Types): All Purpose Flour, Whole Wheat Flour, Pastry Flour, Artisan (Bread) Flour
Size: 1 KG / 5 KG / 25 KG

Flour is good for: Cookies, Cakes, Bread, Biscuits, Brownies, Muffins, Pastries, Pancakes, Rolls, Pizza Crust Pies

Target Market(s)

Fit Lifestyle, Hipsters, Modern, NYC

Industry/Entity Type

Agtech

Logo Text

Nonna's Granary

Requirements
Must have
• Nonna's Pic must be incorporated somehow on the bag. He will provide a friendly face and a homier feeling. The pic does not need to be the Center Piece. The logo will be the Center Piece.
Nice to have
• Nonna's Granary on the side of the bags or some cool/hip design.

```html
<!DOCTYPE html>
<html lang="en">
<head>
<meta charset="utf-8">
<title>Nonna's Granary – Flour Bag Front</title>
<link rel="stylesheet" href="https://fonts.googleapis.com/css2?family=Kanit:ital,wght@0,700;1,500;1,600;1,700&display=swap">
<style>
  :root {
    --backdrop: #e6e6e6;
    --kraft: #c9b99d;
    --kraft-light: #d4c5aa;
    --ink: #1c1714;
    --portrait-tone: #4a3f36;
  }
  * { margin: 0; padding: 0; box-sizing: border-box; }
  html, body {
    width: 1200px; height: 1200px; overflow: hidden;
    background: var(--backdrop);
    font-family: "Kanit", sans-serif;
    color: var(--ink);
  }
  .bag-front {
    position: absolute; left: 345px; top: 205px;
    width: 510px; height: 790px;
    background: linear-gradient(180deg, var(--kraft-light), var(--kraft));
  }
  .founder-portrait {
    position: absolute; left: 344px; top: 12px;
    width: 120px; height: 136px;
    border-radius: 48% 52% 40% 45%;
    background: radial-gradient(circle at 50% 45%, #6b5a4c, var(--portrait-tone));
  }
  .brand-name {
    position: absolute; left: 60px; top: 150px; width: 390px;
    text-align: center; font-weight: 700; font-style: normal;
    line-height: 0.95;
  }
  .brand-name .first { display: block; font-size: 84px; }
  .brand-name .second { display: block; font-size: 46px; }
  .claims {
    position: absolute; left: 0; width: 510px; top: 310px;
    text-align: center; font-size: 10.5px; font-style: italic; font-weight: 600;
  }
  .claims-rule {
    position: absolute; left: 150px; top: 334px; width: 210px; height: 1px;
    background: var(--ink);
  }
  .product-types { position: absolute; left: 38px; top: 357px; list-style: none; }
  .product-types li {
    display: flex; align-items: center; height: 18.5px;
    font-size: 14px; font-style: italic; font-weight: 600;
  }
  .product-types .box {
    width: 11px; height: 11px; border: 1.3px solid var(--ink);
    margin-right: 15px;
  }
  .size-badge {
    position: absolute; left: 344px; top: 398px;
    width: 84px; height: 84px; border-radius: 50%;
    background: var(--ink); color: var(--kraft-light);
    display: flex; align-items: center; justify-content: center;
    font-size: 18px; font-style: italic; font-weight: 700;
  }
  .uses-marker {
    position: absolute; left: 0; top: 494px; width: 64px; height: 64px;
    background: var(--ink);
  }
  .uses {
    position: absolute; left: 70px; top: 498px;
    font-size: 14.5px; font-style: italic; font-weight: 700; line-height: 17.5px;
  }
</style>
</head>
<body>
  <main class="bag-front">
    <div class="founder-portrait" role="img" aria-label="Portrait of the family's grandfather in a flat cap"></div>

    <h1 class="brand-name"><span class="first">Nonna's</span><span class="second">Granary</span></h1>

    <p class="claims">100% Organic | Non GMO | Family Owned | Stone Milled</p>
    <div class="claims-rule"></div>

    <ul class="product-types">
      <li><span class="box"></span>All Purpose Flour</li>
      <li><span class="box"></span>Whole Wheat Flour</li>
      <li><span class="box"></span>Pastry Flour</li>
      <li><span class="box"></span>Artisan (Bread) Flour</li>
    </ul>

    <div class="size-badge">1 KG</div>

    <div class="uses-marker"></div>
    <div class="uses">
      Flour is good for:<br>
      Cookies, Cakes, Bread, Biscuits, Brownies<br>
      Muffins, Pastries, Pancakes<br>
      Rolls, Pizza Crust Pies
    </div>
  </main>
</body>
</html>
```